New Business Card Design Project

I would like a business card to match my truck wrap and logo. I would like the font to match my existing business card please.

Industry/Entity Type

Painter

Contact Information for Business Card

Rodrigo Venter 801-437-2910 Ventercoatings.utah@brushmail.net
SERVICES - Custom Paint & Stain, Interior & Exterior, Epoxy Coatings / Garage Floors, Cabinet Refinishing, Log Staining and Refinishing.

Requirements
Nice to have
• I would like to have the white and grey line like the bottom of my vehicle wrap, Light Grey to match my truck also.

```html
<!DOCTYPE html>
<html lang="en">
<head>
<meta charset="utf-8">
<title>Venter Coatings Business Card</title>
<link rel="stylesheet" href="https://fonts.googleapis.com/css2?family=Archivo+Black&family=Arimo:wght@400&display=swap">
<style>
  :root {
    --page: #2a2a2a;
    --blue-light: #03a9e9;
    --blue-deep: #0f5a98;
    --brand-blue: #12a3e3;
    --ring-grey: #b3b6c1;
    --white: #ffffff;
  }
  * { box-sizing: border-box; margin: 0; padding: 0; }
  html, body { width: 1200px; height: 1015px; overflow: hidden; }
  body {
    background: var(--page);
    font-family: "Arimo", Arial, sans-serif;
    display: flex;
    flex-direction: column;
    align-items: center;
    justify-content: center;
    gap: 45px;
  }
  .card {
    position: relative;
    width: 700px;
    height: 400px;
    overflow: hidden;
    box-shadow: 0 10px 30px rgba(0,0,0,.5);
  }
  .card-bg { position: absolute; inset: 0; }
  .brand {
    position: absolute;
    left: 420px;
    top: 78px;
    display: flex;
    align-items: center;
    gap: 12px;
  }
  .brand-mark {
    width: 40px; height: 40px;
    background: var(--brand-blue);
    border-radius: 6px;
  }
  .brand-name {
    font-family: "Archivo Black", "Arial Black", sans-serif;
    color: var(--brand-blue);
    font-size: 27px;
    line-height: 1.05;
    text-transform: uppercase;
  }
  .services {
    position: absolute;
    left: 48px;
    top: 112px;
    list-style: none;
    color: var(--white);
    font-size: 18px;
    line-height: 29px;
  }
  .services li { position: relative; padding-left: 30px; }
  .services li::before {
    content: "";
    position: absolute;
    left: 2px; top: 9px;
    width: 11px; height: 11px;
    background: var(--white);
    transform: rotate(45deg);
    border-radius: 2px;
  }
  .services .cont { padding-left: 30px; }
  .services .cont::before { display: none; }
  .holder-name {
    position: absolute;
    left: 50px;
    top: 100px;
    font-family: "Archivo Black", "Arial Black", sans-serif;
    color: var(--white);
    font-size: 23px;
    text-transform: uppercase;
  }
  .contact {
    position: absolute;
    left: 50px;
    bottom: 36px;
    list-style: none;
    color: var(--white);
    font-size: 17px;
    line-height: 26px;
  }
  .contact li { display: flex; align-items: center; gap: 10px; }
  .contact svg { width: 16px; height: 16px; fill: var(--white); flex: none; }
</style>
</head>
<body>

<section class="card card-front">
  <svg class="card-bg" viewBox="0 0 700 400" preserveAspectRatio="none" aria-hidden="true">
    <defs>
      <linearGradient id="blueFront" x1="0" y1="0" x2="0" y2="1">
        <stop offset="0" stop-color="#03a9e9"/>
        <stop offset="1" stop-color="#0f5a98"/>
      </linearGradient>
    </defs>
    <rect width="700" height="400" fill="url(#blueFront)"/>
    <circle cx="507" cy="112" r="211" fill="#b3b6c1"/>
    <circle cx="517" cy="104" r="208" fill="#ffffff"/>
  </svg>
  <ul class="services">
    <li>Custom Paint &amp; Stain</li>
    <li>Interior &amp; Exterior</li>
    <li>Epoxy Coatings</li>
    <li>Garage Floors</li>
    <li>Cabinet Refinishing</li>
    <li>Log Staining and</li>
    <li class="cont">Refinishing.</li>
  </ul>
  <div class="brand">
    <span class="brand-mark"></span>
    <span class="brand-name">Venter<br>Coatings</span>
  </div>
</section>

<section class="card card-back">
  <svg class="card-bg" viewBox="0 0 700 400" preserveAspectRatio="none" aria-hidden="true">
    <defs>
      <linearGradient id="blueBack" x1="0" y1="0" x2="0" y2="1">
        <stop offset="0" stop-color="#03a9e9"/>
        <stop offset="1" stop-color="#0f5a98"/>
      </linearGradient>
    </defs>
    <rect width="700" height="400" fill="url(#blueBack)"/>
    <circle cx="507" cy="112" r="211" fill="#b3b6c1"/>
    <circle cx="517" cy="104" r="208" fill="#ffffff"/>
  </svg>
  <h1 class="holder-name">Rodrigo Venter</h1>
  <ul class="contact">
    <li>
      <svg viewBox="0 0 24 24" aria-hidden="true"><path d="M6.6 10.8a15.1 15.1 0 0 0 6.6 6.6l2.2-2.2c.3-.3.7-.4 1-.2 1.1.4 2.3.6 3.6.6.6 0 1 .4 1 1V20c0 .6-.4 1-1 1A17 17 0 0 1 3 4c0-.6.4-1 1-1h3.5c.6 0 1 .4 1 1 0 1.3.2 2.5.6 3.6.1.3 0 .7-.2 1z"/></svg>
      801-437-2910
    </li>
    <li>
      <svg viewBox="0 0 24 24" aria-hidden="true"><path d="M2 5h20v14H2z"/><path d="M3 6l9 7 9-7" fill="none" stroke="#0f5a98" stroke-width="1.5"/></svg>
      Ventercoatings.utah@brushmail.net
    </li>
  </ul>
  <div class="brand">
    <span class="brand-mark"></span>
    <span class="brand-name">Venter<br>Coatings</span>
  </div>
</section>

</body>
</html>
```